Chart Your Own Harbor Promotional Flyer

I Need a one page, one-sided 8.5 x 11 editable promotional flyer that POPS!, designed in photoshop

[TITLE]Chart Your Own Harbor: 3 BRIGHT Steps to Lift Your Practice Today!

[CONTENT for the Flyer:]

At this content-rich event you will learn how to:
• Get out of feast and famine mode and into six, multi-six and/or seven figure-income mode
• Leapfrog your competition and become the obvious choice in your market
• Have your business aligned with who you are and what you want
• Enjoy your business far more than you imagined possible.
• Have more fun and time to yourself
• Live free and unbound!

Accolades
“Delphine helped us increase our six figure income by 41%...I feel reborn!” Marlene & Otis Pruitt, Vienna, VA

“…Delphine is a joy to listen to - compelling, smart, provocative…” – Dwight Fennimore, Charlotte, North Carolina

“Delphine helped me increase my business by 66%...without me spending more time, money, or making cold calls! …I am in the zone!” Tess Calloway, Baltimore, MD
“Delphine is an energetic and dynamic speaker…content-rich…holds your attention to the very end!” Hal Brisbee, Frmr Pres., Kemper & Vail, MD, MD, D.C., PA, DE, NJ
“Delphine is the real estate whisperer!” Lou Tremaine, Washington D.C.

“Delphine was prepared, funny, informative and made a connection with each of our agents…Fabulous!…even my admins were PUMPED!!! – Paul Devereux, New York

About Delphine:
Delphine is a highly regarded business development speaker & coach who knows how to pump up an audience and have them making more money, in less time, AND having more fun doing it! What’s not to love?! Consistently rated as an exceptional speaker and conference favorite! Among her work: Magnet Method: How to Draw Your Dream Buyers Time After Time!, Client Pipelines Without Fuss, The Costliest Outreach Blunders Real Estate Agents Commit and How to Sidestep Them, Hard Seasons Forge Hard Sellers, Fuel for the Spirit for Real Estate Agents.

[Also need a section for:]
Date: December 9, 2015, Time: 9:00 Am - 12:00 Noon, Place: Silver Maple Conference, Ashford Hollow, PA

Target Market(s)

Real Estate Agents

Industry/Entity Type

Real Estate Agent

Font styles to use
Sans Serif

Colors
0655a3
f37122

Requirements
Must have
• the top tier prop mentor logo
Nice to have
• chart your own harbor logo; lots of POP! :-) ; open to other colors, accent colors.

```html
<!DOCTYPE html>
<html lang="en">
<head>
<meta charset="utf-8">
<title>Chart Your Own Harbor – Event Flyer</title>
<link rel="stylesheet" href="https://fonts.googleapis.com/css2?family=Mulish:ital,wght@0,300;0,400;0,700;0,800;0,900;1,300;1,400&family=Arimo:ital,wght@0,400;0,700;1,400&display=swap">
<style>
  :root {
    --orange: #f37122;
    --orange-bright: #ff7409;
    --navy: #132456;
    --ink: #111111;
    --paper: #ffffff;
    --stage: #e4e4e4;
  }
  * { margin: 0; padding: 0; box-sizing: border-box; }
  html, body { width: 1200px; height: 1200px; overflow: hidden; }
  body { background: var(--stage); position: relative; font-family: "Arimo", Arial, sans-serif; color: var(--ink); }

  .flyer {
    position: absolute; left: 190px; top: 67px; width: 823px; height: 1066px;
    background: radial-gradient(ellipse at 50% 35%, #ffffff 0%, #f6f6f6 55%, #e2e2e2 100%);
    box-shadow: 0 4px 18px rgba(0,0,0,.25);
    overflow: hidden;
  }
  .abs { position: absolute; }

  .headline { left: 0; width: 823px; top: 48px; text-align: center; font-family: "Mulish", sans-serif; font-weight: 900; font-size: 46px; color: var(--orange); letter-spacing: 0.5px; text-shadow: 1px 2px 2px rgba(0,0,0,.25); }
  .subhead-small { left: 0; width: 823px; top: 110px; text-align: center; font-family: "Mulish", sans-serif; font-weight: 800; font-size: 24px; color: var(--navy); }
  .subhead-large { left: 0; width: 823px; top: 136px; text-align: center; font-family: "Mulish", sans-serif; font-weight: 900; font-size: 40px; color: var(--navy); text-shadow: 1px 2px 2px rgba(0,0,0,.2); }

  .side-bar { left: 794px; top: 136px; width: 29px; height: 228px; background: var(--orange-bright); }

  .learn-title { left: 46px; top: 213px; font-size: 17.5px; font-weight: 700; color: var(--orange); letter-spacing: 0.1px; }
  .learn-list { left: 45px; top: 243px; list-style: none; }
  .learn-list li { display: flex; align-items: center; height: 24.2px; font-size: 14.6px; font-weight: 700; color: var(--ink); }
  .learn-list .num { width: 17px; height: 17px; border-radius: 50%; background: var(--navy); color: #fff; font-size: 10px; display: inline-flex; align-items: center; justify-content: center; margin-right: 10px; }

  .portrait { left: 588px; top: 308px; width: 235px; height: 243px; }

  .brand { left: 44px; top: 440px; width: 250px; display: flex; align-items: center; gap: 12px; font-family: "Mulish", sans-serif; font-weight: 700; font-size: 29px; line-height: 1.05; color: var(--navy); }
  .brand .dot { flex: none; width: 14px; height: 14px; border-radius: 50%; background: var(--orange); }

  .coach-name { left: 372px; top: 358px; font-family: "Mulish", sans-serif; font-size: 28px; font-weight: 400; color: #8a8a8a; white-space: nowrap; }
  .coach-mark { left: 318px; top: 394px; font-family: "Mulish", sans-serif; font-weight: 900; color: var(--orange); text-transform: uppercase; white-space: nowrap; }
  .coach-mark .big { display: block; font-size: 54px; line-height: 1; }
  .coach-mark .small { display: block; font-size: 27px; line-height: 1.1; color: var(--navy); letter-spacing: 0.5px; }

  .band { left: 0; top: 551px; width: 823px; height: 208px; background: var(--orange-bright); }
  .tagline-bar { left: 0; top: 553px; width: 823px; height: 54px; }
  .tagline { left: 175px; top: 553px; width: 648px; height: 54px; display: flex; align-items: center; justify-content: center; font-style: italic; font-size: 18px; color: #fff; }

  .quotes { left: 20px; top: 620px; width: 783px; height: 139px; display: flex; }
  .quote { flex: 1; position: relative; display: flex; flex-direction: column; align-items: center; text-align: center; color: #fff; font-family: "Mulish", sans-serif; font-weight: 300; font-size: 12px; line-height: 1.2; padding: 0 18px; }
  .quote::before, .quote:last-child::after { content: ""; position: absolute; top: 53px; bottom: 0; width: 1px; background: rgba(255,255,255,.8); }
  .quote::before { left: 0; }
  .quote:last-child::after { right: 0; }
  .quote svg { margin-bottom: 12px; }
  .quote cite { font-style: italic; display: block; }

  .about-strip { left: 0; top: 759px; width: 28px; height: 167px; background: var(--orange-bright); }
  .about { left: 28px; top: 781px; width: 795px; height: 145px; background: linear-gradient(to bottom, #e6e6e6, #f7f7f7); padding: 21px 30px 0 20px; }
  .about h2 { font-size: 17px; font-weight: 700; text-decoration: underline; color: var(--ink); line-height: 1; margin-bottom: 2px; }
  .about p { font-size: 13px; line-height: 16.2px; text-align: justify; }

  .footer { left: 0; top: 926px; width: 823px; height: 115px; background: var(--navy); color: #fff; font-family: "Mulish", sans-serif; font-weight: 800; }
  .footer-base { left: 0; top: 1041px; width: 823px; height: 25px; background: var(--orange-bright); }
  .footer .divider { position: absolute; left: 410px; top: 16px; width: 1px; height: 83px; background: rgba(255,255,255,.7); }
  .info { position: absolute; top: 24px; font-size: 19px; line-height: 23px; }
  .info h3 { font-size: 19px; font-weight: 800; text-decoration: underline; }
  .info.when { left: 143px; }
  .info.where { left: 541px; }
  .icon { position: absolute; }
</style>
</head>
<body>
  <main class="flyer">
    <h1 class="abs headline">CHART YOUR OWN HARBOR</h1>
    <p class="abs subhead-small">3 BRIGHT STEPS TO</p>
    <p class="abs subhead-large">LIFT YOUR PRACTICE TODAY!</p>
    <div class="abs side-bar"></div>

    <h2 class="abs learn-title">AT THIS CONTENT-RICH EVENT YOU WILL LEARN HOW TO:</h2>
    <ol class="abs learn-list">
      <li><span class="num">1</span>Get out of feast and famine mode and into six, multi-six and/or seven figure-income mode</li>
      <li><span class="num">2</span>Leapfrog your competition and become the obvious choice in your market</li>
      <li><span class="num">3</span>Have your business aligned with who you are and what you want</li>
      <li><span class="num">4</span>Enjoy your business far more than you imagined possible.</li>
      <li><span class="num">5</span>Have more fun and time to yourself</li>
      <li><span class="num">6</span>Live free and unbound!</li>
    </ol>

    <svg class="abs portrait" viewBox="0 0 235 243" role="img" aria-label="Portrait photograph of the coach, Delphine Ashby">
      <defs>
        <linearGradient id="portraitTone" x1="0" y1="0" x2="0" y2="1">
          <stop offset="0" stop-color="#f1f1f1"/>
          <stop offset="1" stop-color="#2a2a2e"/>
        </linearGradient>
      </defs>
      <rect width="235" height="243" fill="url(#portraitTone)"/>
    </svg>

    <div class="abs brand"><span class="dot"></span><span>Chart Your Own Harbor</span></div>

    <p class="abs coach-name">Delphine Ashby</p>
    <p class="abs coach-mark"><span class="big">Top Tier</span><span class="small">Prop Mentor</span></p>

    <div class="abs band"></div>
    <svg class="abs tagline-bar" viewBox="0 0 823 54" preserveAspectRatio="none" aria-hidden="true">
      <polygon points="222,0 823,0 823,54 175,54" fill="#132456"/>
    </svg>
    <p class="abs tagline">“America’s Top Tier Prop Mentor” ™</p>

    <section class="abs quotes">
      <div class="quote">
        <svg width="56" height="44" viewBox="0 0 56 44" aria-hidden="true"><ellipse cx="22" cy="16" rx="21" ry="14" fill="#fff"/><path d="M10 26 L6 38 L20 29 Z" fill="#fff"/><ellipse cx="37" cy="26" rx="17" ry="11" fill="#fff" stroke="#ff7409" stroke-width="3"/><path d="M44 34 L50 42 L38 36 Z" fill="#fff"/></svg>
        <p>“Delphine helped us increase our six figure income by 41%...I feel reborn!”<cite>Marlene &amp; Otis Pruitt,<br>Vienna, VA</cite></p>
      </div>
      <div class="quote">
        <svg width="56" height="44" viewBox="0 0 56 44" aria-hidden="true"><ellipse cx="22" cy="16" rx="21" ry="14" fill="#fff"/><path d="M10 26 L6 38 L20 29 Z" fill="#fff"/><ellipse cx="37" cy="26" rx="17" ry="11" fill="#fff" stroke="#ff7409" stroke-width="3"/><path d="M44 34 L50 42 L38 36 Z" fill="#fff"/></svg>
        <p>“...Delphine is a joy to listen to - compelling, smart, provocative...”<cite>Dwight Fennimore, Charlotte,<br>North Carolina</cite></p>
      </div>
      <div class="quote">
        <svg width="56" height="44" viewBox="0 0 56 44" aria-hidden="true" style="margin-bottom:9px"><ellipse cx="22" cy="16" rx="21" ry="14" fill="#fff"/><path d="M10 26 L6 38 L20 29 Z" fill="#fff"/><ellipse cx="37" cy="26" rx="17" ry="11" fill="#fff" stroke="#ff7409" stroke-width="3"/><path d="M44 34 L50 42 L38 36 Z" fill="#fff"/></svg>
        <p>“Delphine was prepared, funny, informative and made a connection with each of our agents...Fabulous!...even my admins were PUMPED!!!”<cite>Paul Devereux,<br>New York</cite></p>
      </div>
    </section>

    <div class="abs about-strip"></div>
    <section class="abs about">
      <h2>ABOUT DELPHINE</h2>
      <p>Delphine is a highly regarded business development speaker &amp; coach who knows how to pump up an audience and have them making more money, in less time, AND having more fun doing it! What’s not to love?! Consistently rated as an exceptional speaker and conference favorite! Among her work: Magnet Method: How to Draw Your Dream Buyers Time After Time!, Client Pipelines Without Fuss, The Costliest Outreach Blunders Real Estate Agents Commit and How to Sidestep Them, Hard Seasons Forge Hard Sellers, Fuel for the Spirit for Real Estate Agents.</p>
    </section>

    <footer class="abs footer">
      <svg class="icon" style="left:37px;top:23px" width="70" height="70" viewBox="0 0 70 70" aria-hidden="true">
        <circle cx="35" cy="35" r="31" fill="none" stroke="#fff" stroke-width="5"/>
        <path d="M35 35 L35 20 M35 35 L22 40" stroke="#fff" stroke-width="5" stroke-linecap="round"/>
        <circle cx="35" cy="35" r="3.5" fill="#fff"/>
      </svg>
      <div class="info when">
        <h3>DATE &amp; TIME</h3>
        <p>December 9, 2015</p>
        <p>9:00 Am - 12:00 Noon</p>
      </div>
      <div class="divider"></div>
      <svg class="icon" style="left:448px;top:23px" width="62" height="72" viewBox="0 0 62 72" aria-hidden="true">
        <path d="M31 4 C18 4 10 14 10 25 C10 39 31 56 31 56 C31 56 52 39 52 25 C52 14 44 4 31 4 Z" fill="#fff"/>
        <circle cx="31" cy="24" r="8" fill="#132456"/>
        <path d="M16 54 C6 57 4 61 6 64 C10 70 52 70 56 64 C58 61 56 57 46 54" fill="none" stroke="#fff" stroke-width="4"/>
      </svg>
      <div class="info where">
        <h3>LOCATION</h3>
        <p>Silver Maple Conference,</p>
        <p>Ashford Hollow, PA</p>
      </div>
    </footer>
    <div class="abs footer-base"></div>
  </main>
</body>
</html>
```